Dr. Marissa Tevlin Medical/Chiropractic Business Card

Dr. Tevlin is a chiropractor and will require a business card that she uses every single day to book appointments on the back side of the card. Currently the office name goes by Dr. Marissa Tevlin. The chiropractic profession is based on the diagnosis and manipulative treatment of misalignments of the joints, especially those of the spinal column, which are held to cause other disorders by affecting the nerves, muscles, and organs. Dr. Marissa Tevlin is looking for a contemporary and minimalistic design.

Industry/Entity Type

Medical

Contact Information for Business Card

Name: Dr. Marissa Tevlin; Address: 748 Harcastle Rd South, London, ON N5R 2K7; Phone Number: 519.274.6193; Fax: 519.281.5046; email: marissa.tevlin@quorvamail.com

Requirements
Must have
• ability to write multiple appointments date/time on the back of card

```html
<!DOCTYPE html>
<html lang="en">
<head>
<meta charset="utf-8">
<title>Dr. Marissa Tevlin – Business Card</title>
<link href="https://fonts.googleapis.com/css2?family=Questrial&display=swap" rel="stylesheet">
<style>
  :root {
    --page-bg: #e9e7e3;
    --card-white: #ffffff;
    --card-grey: #f1f1f1;
    --royal-blue: #3b55c6;
    --deep-blue: #2c40ad;
    --cyan: #35c1e2;
    --text-grey: #6b6b6b;
    --rule-grey: #c9c9c9;
    --white-text: #ffffff;
  }
  * { margin: 0; padding: 0; box-sizing: border-box; }
  html, body {
    width: 1200px; height: 973px; overflow: hidden;
    background: var(--page-bg);
    font-family: "Questrial", "Century Gothic", sans-serif;
  }
  .stage {
    width: 1200px; height: 973px;
    display: flex; justify-content: center; align-items: center; gap: 90px;
  }
  .card {
    position: relative;
    width: 380px; height: 660px;
    border-radius: 26px;
    overflow: hidden;
    box-shadow: 0 10px 30px rgba(0,0,0,.18);
  }

  /* Front */
  .card-front { background: var(--card-white); }
  .front-bg { position: absolute; inset: 0; }
  .brand {
    position: absolute; top: 120px; left: 0; right: 0;
    display: flex; align-items: center; justify-content: center; gap: 12px;
    color: var(--royal-blue); font-size: 22px;
  }
  .brand-square { width: 22px; height: 22px; background: var(--cyan); border-radius: 4px; }
  .contact-block {
    position: absolute; left: 36px; bottom: 30px;
    height: 320px;
    writing-mode: vertical-rl;
    transform: rotate(180deg);
    color: var(--white-text);
  }
  .doctor-name { font-size: 28px; opacity: .85; letter-spacing: -.3px; line-height: 1.15; }
  .doctor-title { font-size: 18px; color: var(--cyan); margin-inline-start: 0; margin-block-end: 22px; letter-spacing: .5px; }
  .contact-line {
    display: flex; align-items: center; gap: 8px;
    font-size: 16px; line-height: 1.5;
    padding-inline-start: 50px;
  }
  .contact-line svg { width: 13px; height: 13px; flex: none; }
  .address { font-size: 16px; line-height: 1.35; margin-block-start: 14px; padding-inline-start: 80px; }

  /* Back */
  .card-back {
    background: linear-gradient(160deg, var(--card-white) 0%, var(--card-grey) 100%);
    padding: 40px 34px 0;
  }
  .back-brand {
    display: flex; align-items: center; justify-content: center; gap: 10px;
    color: var(--royal-blue); font-size: 17px; margin-top: 10px;
  }
  .back-brand .brand-square { width: 16px; height: 16px; }
  .appointments-title {
    text-align: center; font-size: 30px; font-weight: 400; color: var(--text-grey);
    margin-top: 22px; letter-spacing: 1px;
  }
  .schedule {
    display: grid; grid-template-columns: 1.3fr 1fr; column-gap: 24px;
    margin-top: 20px;
  }
  .schedule-head {
    font-size: 20px; color: var(--text-grey);
    border-bottom: 2px solid var(--cyan); padding-bottom: 2px;
  }
  .schedule-row { height: 38px; border-bottom: 1px solid var(--rule-grey); }
  .schedule-row.last { border-bottom: 2px solid var(--cyan); }
  .reschedule-note {
    text-align: center; font-size: 15px; color: #a8a8a8;
    margin-top: 14px; line-height: 1.35;
  }
</style>
</head>
<body>
<main class="stage">

  <section class="card card-front" aria-label="Card front">
    <svg class="front-bg" viewBox="0 0 380 660" preserveAspectRatio="none" aria-hidden="true">
      <defs>
        <linearGradient id="blueFill" x1="0" y1="0" x2="1" y2="1">
          <stop offset="0" stop-color="#2f46b3"/>
          <stop offset=".5" stop-color="#4262cf"/>
          <stop offset="1" stop-color="#2c40ad"/>
        </linearGradient>
      </defs>
      <path d="M0 270 Q170 330 380 150 L380 660 L0 660 Z" fill="var(--cyan)"/>
      <path d="M0 290 Q190 355 380 170 L380 660 L0 660 Z" fill="url(#blueFill)"/>
    </svg>
    <div class="brand"><span class="brand-square"></span>Tevlin Chiropractic</div>

    <div class="contact-block">
      <p class="doctor-name">Dr. Marissa Tevlin</p>
      <p class="doctor-title">Chiropractor</p>
      <p class="contact-line">
        <svg viewBox="0 0 14 14"><path d="M3 1h3l1 3-2 1.5a8 8 0 0 0 3.5 3.5L10 7l3 1v3a2 2 0 0 1-2 2A11 11 0 0 1 1 3a2 2 0 0 1 2-2z" fill="var(--cyan)"/></svg>
        519.274.6193
      </p>
      <p class="contact-line">
        <svg viewBox="0 0 14 14"><rect x="1" y="5" width="12" height="7" rx="1" fill="var(--cyan)"/><rect x="4" y="1" width="6" height="5" fill="var(--cyan)"/></svg>
        519.281.5046
      </p>
      <p class="contact-line">
        <svg viewBox="0 0 14 14"><rect x="1" y="3" width="12" height="8" fill="var(--cyan)"/><path d="M1 3l6 5 6-5" stroke="#fff" fill="none"/></svg>
        marissa.tevlin@quorvamail.com
      </p>
      <p class="address">748 Harcastle Rd South,<br>London, ON N5R 2K7</p>
    </div>
  </section>

  <section class="card card-back" aria-label="Card back">
    <div class="back-brand"><span class="brand-square"></span>Tevlin Chiropractic</div>
    <h2 class="appointments-title">Appointments</h2>
    <div class="schedule">
      <div class="schedule-head">Date</div>
      <div class="schedule-head">Time</div>
      <div class="schedule-row"></div><div class="schedule-row"></div>
      <div class="schedule-row"></div><div class="schedule-row"></div>
      <div class="schedule-row"></div><div class="schedule-row"></div>
      <div class="schedule-row"></div><div class="schedule-row"></div>
      <div class="schedule-row"></div><div class="schedule-row"></div>
      <div class="schedule-row"></div><div class="schedule-row"></div>
      <div class="schedule-row"></div><div class="schedule-row"></div>
      <div class="schedule-row"></div><div class="schedule-row"></div>
      <div class="schedule-row last"></div><div class="schedule-row last"></div>
    </div>
    <p class="reschedule-note">If you are unable to make your appointment,<br>please call us to reschedule</p>
  </section>

</main>
</body>
</html>
```